Harrowmere Sack operates across the US and Australasia providing calico bags to small business through to large enterprise across all verticals. Our bags are the most premium in the market place and our customer service is second to none. Our competitive advantage lays in our competitive pricing, superior quality and outstanding customer service.

Industry/Entity Type

Business

Contact Information for Business Card

Harrowmere Sack
Delphine Marrow
Managing Director
delphine@harrowmeresack.com
www.harrowmeresack.com.au
Mobile:- 0417 689 305
Level 3, 248 Pembury Street
Melbourne Victoria Australia 3008

```html
<!DOCTYPE html>
<html lang="en">
<head>
<meta charset="utf-8">
<title>Harrowmere Sack business cards</title>
<link rel="stylesheet" href="https://fonts.googleapis.com/css2?family=Tinos:ital,wght@0,400;0,700;1,400&display=swap">
<style>
  :root {
    --page: #f1e9e8;
    --green: #047a04;
    --black: #030303;
    --paper: #f5edeb;
    --ink: #111111;
  }
  * { margin: 0; padding: 0; box-sizing: border-box; }
  html, body { width: 1200px; height: 1200px; overflow: hidden; background: var(--page); }
  body { position: relative; font-family: "Tinos", "Times New Roman", serif; }

  .card { position: absolute; width: 488px; height: 312px; overflow: hidden; }
  .col-front { left: 74px; }
  .col-back { left: 634px; }
  .row-1 { top: 94px; }
  .row-2 { top: 452px; }
  .row-3 { top: 806px; }

  .front-green { background: var(--green); }
  .front-black { background: var(--black); }
  .front-paper { background: var(--paper); }

  .map-area {
    position: absolute; left: 108px; top: 28px; width: 276px; height: 258px;
    border-radius: 60px 40px 70px 90px;
  }
  .map-light { background: var(--paper); }
  .map-green { background: var(--green); }

  .front-name {
    position: absolute; left: 108px; top: 128px; width: 276px;
    text-align: center; font-weight: 700; font-size: 24px; letter-spacing: 1px;
  }
  .name-dark { color: var(--black); }
  .name-light { color: var(--paper); }

  .back-shape { position: absolute; inset: 0; width: 488px; height: 312px; }

  .back-heading {
    position: absolute; right: 40px; top: 40px;
    font-weight: 700; font-size: 27px; letter-spacing: -0.3px; white-space: nowrap;
  }
  .contact, .address {
    position: absolute; right: 40px; text-align: right;
    font-size: 15px; line-height: 19px; white-space: nowrap;
  }
  .contact { top: 92px; }
  .address { top: 170px; }
  .person { position: absolute; left: 40px; top: 206px; font-size: 15.5px; line-height: 20px; }
  .person .person-name { font-weight: 700; }
  .person .person-role { font-style: italic; }

  .text-light { color: var(--paper); }
  .text-dark { color: var(--ink); }
</style>
</head>
<body>

  <!-- Front, green -->
  <div class="card front-green col-front row-1">
    <div class="map-area map-light" role="img" aria-label="Map of Australia silhouette"></div>
    <div class="front-name name-dark">HARROWMERE SACK</div>
  </div>

  <!-- Back, black and green -->
  <div class="card col-back row-1" style="background: var(--black);">
    <svg class="back-shape" viewBox="0 0 488 312" aria-hidden="true">
      <path d="M110,0 H488 V312 H158 C206,282 206,232 184,202 C146,152 60,126 62,62 C64,26 84,6 110,0 Z" fill="var(--green)"/>
    </svg>
    <div class="back-heading text-light">HARROWMERE SACK</div>
    <div class="contact text-light">delphine@harrowmeresack.com<br>www.harrowmeresack.com.au<br>Mobile: -0417 689 305</div>
    <div class="address text-light">Level 3,<br>248 Pembury Street<br>Melbourne Victoria<br>Australia 3008</div>
    <div class="person text-light"><div class="person-name">Delphine Marrow</div><div class="person-role">Managing Director</div></div>
  </div>

  <!-- Front, black -->
  <div class="card front-black col-front row-2">
    <div class="map-area map-light" role="img" aria-label="Map of Australia silhouette"></div>
    <div class="front-name name-dark">HARROWMERE SACK</div>
  </div>

  <!-- Back, black and paper -->
  <div class="card col-back row-2" style="background: var(--black);">
    <svg class="back-shape" viewBox="0 0 488 312" aria-hidden="true">
      <path d="M110,0 H488 V312 H158 C206,282 206,232 184,202 C146,152 60,126 62,62 C64,26 84,6 110,0 Z" fill="var(--paper)"/>
    </svg>
    <div class="back-heading text-dark">HARROWMERE SACK</div>
    <div class="contact text-dark">delphine@harrowmeresack.com<br>www.harrowmeresack.com.au<br>Mobile: -0417 689 305</div>
    <div class="address text-dark">Level 3,<br>248 Pembury Street<br>Melbourne Victoria<br>Australia 3008</div>
    <div class="person text-light"><div class="person-name">Delphine Marrow</div><div class="person-role">Managing Director</div></div>
  </div>

  <!-- Front, paper -->
  <div class="card front-paper col-front row-3">
    <div class="map-area map-green" role="img" aria-label="Map of Australia silhouette"></div>
    <div class="front-name name-light">HARROWMERE SACK</div>
  </div>

  <!-- Back, paper and green -->
  <div class="card col-back row-3" style="background: var(--paper);">
    <svg class="back-shape" viewBox="0 0 488 312" aria-hidden="true">
      <path d="M110,0 H488 V312 H158 C206,282 206,232 184,202 C146,152 60,126 62,62 C64,26 84,6 110,0 Z" fill="var(--green)"/>
    </svg>
    <div class="back-heading text-light">HARROWMERE SACK</div>
    <div class="contact text-light">delphine@harrowmeresack.com<br>www.harrowmeresack.com.au<br>Mobile: -0417 689 305</div>
    <div class="address text-light">Level 3,<br>248 Pembury Street<br>Melbourne Victoria<br>Australia 3008</div>
    <div class="person text-dark"><div class="person-name">Delphine Marrow</div><div class="person-role">Managing Director</div></div>
  </div>

</body>
</html>
```